Marrowfield Dental
Professional
Dr. Lien Vu
Marrowfield Dental - (Business name)
418-265 West Harlow St.
Vancouver, BC
V6R 2K8
info@coastal-smilecare-bc.ca
www.coastal-smilecare-bc.ca
Logo of Marrowfield Dental
Name, address, phone #.... smaller in corner maybe? Use logo designed.
Your next appointment:_________________
at _______am/pm.
See you soon!
(something like that)
Vector logo
Vector logo (wide)

```html
<!DOCTYPE html>
<html lang="en">
<head>
<meta charset="utf-8">
<title>Marrowfield Dental – Business Card</title>
<link href="https://fonts.googleapis.com/css2?family=Source+Sans+3:wght@400;600;700&display=swap" rel="stylesheet">
<style>
  :root {
    --sheet: #ffffff;
    --card-blue: #2bb3e2;
    --card-blue-light: #5cc8ee;
    --card-blue-deep: #1e9fd0;
    --emblem: #74d0f1;
    --rule: rgba(255,255,255,0.55);
    --ink: #ffffff;
    --crop: #222222;
  }
  * { margin: 0; padding: 0; box-sizing: border-box; }
  html, body { width: 1200px; height: 936px; overflow: hidden; }
  body {
    background: var(--sheet);
    position: relative;
    font-family: "Source Sans 3", "Myriad Pro", Arial, sans-serif;
    color: var(--ink);
  }
  .crop-marks { position: absolute; inset: 0; }
  .card {
    position: absolute;
    top: 56px;
    width: 442px;
    height: 781px;
  }
  .card--front { left: 117px; }
  .card--back { left: 636px; }
  .card__bg { position: absolute; inset: 0; }

  .emblem-name {
    position: absolute;
    left: 0; right: 0;
    top: 330px;
    text-align: center;
    font-weight: 700;
    font-size: 40px;
    letter-spacing: 1px;
    line-height: 1;
  }
  .dentist-name {
    position: absolute;
    right: 36px;
    top: 455px;
    font-size: 22px;
    font-weight: 400;
  }
  .contact-rule {
    position: absolute;
    left: 96px; right: 0;
    height: 1px;
    background: var(--rule);
  }
  .contact {
    position: absolute;
    font-size: 14.5px;
    line-height: 1.4;
  }
  .contact--email { left: 216px; top: 519px; }
  .contact--phones { left: 96px; top: 580px; }
  .contact--address { left: 216px; top: 556px; }
  .contact--web { left: 216px; top: 663px; }

  .appointment {
    position: absolute;
    left: 130px;
    top: 398px;
    font-size: 14.5px;
    line-height: 1.45;
  }
  .appointment p + p { margin-top: 20px; }
</style>
</head>
<body>

<svg class="crop-marks" width="1200" height="936" viewBox="0 0 1200 936" aria-hidden="true">
  <g stroke="var(--crop)" stroke-width="1.5">
    <line x1="117" y1="0" x2="117" y2="40"/><line x1="559" y1="0" x2="559" y2="40"/>
    <line x1="636" y1="0" x2="636" y2="40"/><line x1="1078" y1="0" x2="1078" y2="40"/>
    <line x1="117" y1="853" x2="117" y2="936"/><line x1="559" y1="853" x2="559" y2="936"/>
    <line x1="636" y1="853" x2="636" y2="936"/><line x1="1078" y1="853" x2="1078" y2="936"/>
    <line x1="60" y1="56" x2="100" y2="56"/><line x1="60" y1="837" x2="100" y2="837"/>
    <line x1="1095" y1="56" x2="1140" y2="56"/><line x1="1095" y1="837" x2="1140" y2="837"/>
  </g>
</svg>

<section class="card card--front">
  <svg class="card__bg" width="442" height="781" viewBox="0 0 442 781">
    <rect width="442" height="781" fill="var(--card-blue)"/>
    <path d="M0 0 H60 C40 60 20 120 14 200 V781 H0 Z" fill="var(--card-blue-light)"/>
    <path role="img" aria-label="Flowing line pattern" d="M0 560 C90 640 220 690 442 700 V781 H0 Z" fill="var(--card-blue-deep)" opacity="0.45"/>
    <circle cx="287" cy="209" r="125" fill="var(--emblem)"/>
  </svg>
  <div class="emblem-name">Marrowfield Dental</div>
  <div class="dentist-name">Dr. Lien Vu</div>
  <div class="contact-rule" style="top:505px"></div>
  <div class="contact contact--email">info@coastal-smilecare-bc.ca</div>
  <div class="contact-rule" style="top:547px"></div>
  <div class="contact contact--phones">• 604-555-0142<br>• 604-555-0198</div>
  <div class="contact contact--address">418-265 West Harlow St.<br>Vancouver, BC<br>V6R 2K8</div>
  <div class="contact-rule" style="top:650px"></div>
  <div class="contact contact--web">www.coastal-smilecare-bc.ca</div>
</section>

<section class="card card--back">
  <svg class="card__bg" width="442" height="781" viewBox="0 0 442 781">
    <rect width="442" height="781" fill="var(--card-blue)"/>
    <path d="M0 0 H60 C40 60 20 120 14 200 V781 H0 Z" fill="var(--card-blue-light)"/>
    <circle cx="250" cy="190" r="130" fill="var(--emblem)" opacity="0.35"/>
    <path role="img" aria-label="Flowing line pattern" d="M0 560 C90 640 220 690 442 700 V781 H0 Z" fill="var(--card-blue-deep)" opacity="0.45"/>
  </svg>
  <div class="appointment">
    <p>Your next<br>appointment:_______________<br>at ________am/pm.</p>
    <p>See you soon!<br>(something like that)</p>
  </div>
</section>

</body>
</html>
```